Flyer-Design für Immobilienmakler
Zielgruppe
Wir sind seit 1992 Immobilienmakler und möchten einen Flyer zur Präsentation unserer Firma und Objektakquise gestalten lassen.
Dieser soll einen Gutschein für eine kostenlose Immobilienbewertung enthalten.
Aufgabenstellung
Wir lassen uns dann überraschen

```html
<!DOCTYPE html>
<html lang="de">
<head>
<meta charset="utf-8">
<title>Gutschein Immobilienbewertung</title>
<link href="https://fonts.googleapis.com/css2?family=Montserrat:wght@800&family=Questrial&display=swap" rel="stylesheet">
<style>
  :root {
    --ink: #1f1f1f;
    --yellow: #ffcc00;
    --paper: #ffffff;
    --field: #ececec;
    --sky-top: #2f7fd8;
    --sky-low: #9cc6ee;
    --lawn: #5f9a3a;
    --stage: #f1f1f1;
  }
  * { box-sizing: border-box; margin: 0; padding: 0; }
  html, body { width: 1200px; height: 1200px; overflow: hidden; }
  body {
    background: var(--stage);
    font-family: "Questrial", sans-serif;
    color: var(--ink);
    position: relative;
  }
  .card {
    position: absolute;
    left: 210px;
    width: 780px;
    height: 553px;
    overflow: hidden;
    background: var(--paper);
    box-shadow: 0 10px 28px rgba(0,0,0,.18);
  }
  .card--front { top: 36px; }
  .card--back { top: 611px; }

  /* Front */
  .hero-photo {
    position: absolute; left: 0; top: 0; width: 780px; height: 436px;
    background: linear-gradient(180deg, var(--sky-top) 0%, var(--sky-low) 45%, #c9c2b4 62%, #8c8478 72%, var(--lawn) 86%, #4a7f2c 100%);
  }
  .voucher-label {
    position: absolute; left: 0; top: 80px; width: 360px; height: 90px;
    background: var(--yellow);
    font-family: "Montserrat", sans-serif; font-weight: 800;
    font-size: 56px; line-height: 90px; padding-left: 14px;
    letter-spacing: 1px;
  }
  .offer-panel {
    position: absolute; left: 408px; top: 300px; width: 350px; height: 136px;
    background: rgba(255,255,255,.78);
    transform: rotate(-5deg);
    padding: 14px 0 0 30px;
    line-height: 1;
  }
  .offer-panel .offer-intro { font-size: 26px; padding-left: 74px; }
  .offer-panel .offer-main { font-size: 38px; letter-spacing: .5px; }
  .offer-panel .offer-main em { font-style: normal; color: var(--yellow); }
  .offer-panel .offer-value { font-size: 18px; font-style: italic; padding-left: 64px; margin-top: 2px; }
  .accent-band { position: absolute; left: 0; top: 436px; width: 780px; height: 25px; background: var(--yellow); }
  .footer-band { position: absolute; left: 0; top: 461px; width: 780px; height: 92px; background: var(--ink); }
  .logo-dot {
    position: absolute; left: 396px; top: 484px; width: 46px; height: 46px; border-radius: 50%;
    background: var(--paper); color: var(--ink);
    font-size: 10px; font-style: italic; text-align: center; line-height: 46px;
  }
  .tagline { position: absolute; left: 462px; top: 494px; color: var(--paper); font-size: 21px; }

  /* Back */
  .divider { position: absolute; left: 390px; top: 0; width: 1px; height: 526px; background: #cfcfcf; }
  .intro-text { position: absolute; left: 46px; top: 30px; font-size: 13px; line-height: 16px; text-transform: uppercase; }
  .request-bar {
    position: absolute; left: 0; top: 88px; width: 390px; height: 23px;
    background: var(--ink); color: var(--paper);
    font-size: 12px; line-height: 23px; padding-left: 46px;
  }
  .option { position: absolute; left: 46px; display: flex; align-items: center; font-size: 18px; }
  .option .tick-box { width: 25px; height: 25px; border: 3px solid var(--yellow); margin-right: 15px; }
  .field { position: absolute; left: 46px; width: 328px; height: 21px; background: var(--field); }
  .field-label { position: absolute; left: 46px; font-size: 10px; }
  .stamp-box {
    position: absolute; left: 674px; top: 33px; width: 90px; height: 116px; background: var(--ink);
    color: var(--paper); font-size: 8px; text-align: center; line-height: 116px;
  }
  .reply-service { position: absolute; left: 411px; top: 148px; font-size: 15px; line-height: 18px; }
  .reply-service span { font-style: italic; display: block; }
  .client-logo {
    position: absolute; left: 419px; top: 222px; width: 108px; height: 108px; border-radius: 50%;
    background: var(--ink); color: var(--paper); font-size: 8px; text-align: center; line-height: 108px;
  }
  .address { position: absolute; left: 411px; top: 384px; font-size: 28px; line-height: 31px; }
  .back-band { position: absolute; left: 0; top: 526px; width: 780px; height: 27px; background: var(--ink); }
</style>
</head>
<body>
  <section class="card card--front">
    <div class="hero-photo" role="img" aria-label="Foto eines großen Einfamilienhauses mit Garagen, Rasen und Bäumen unter blauem Himmel"></div>
    <div class="voucher-label">GUTSCHEIN</div>
    <div class="accent-band"></div>
    <div class="offer-panel">
      <p class="offer-intro">Kostenlose</p>
      <p class="offer-main">BEWERTUNG</p>
      <p class="offer-main">IHRER <em>IMMOBILIE</em></p>
      <p class="offer-value">*Im Wert von 800€</p>
    </div>
    <div class="footer-band"></div>
    <div class="logo-dot">Ihr Logo</div>
    <p class="tagline">Ihr Immobilienmakler seit 1992</p>
  </section>

  <section class="card card--back">
    <p class="intro-text">Gerne stellen wir Ihnen aktuelle<br>Informationen zum Immobilienmarkt<br>in Ihrer Region zur Verfügung.</p>
    <p class="request-bar">Ja, bitte senden Sie mir Informationen zu!</p>
    <div class="option" style="top:162px"><span class="tick-box"></span>Immobilien verkaufen/vermieten</div>
    <div class="option" style="top:218px"><span class="tick-box"></span>Immobilien kaufen/mieten</div>
    <div class="option" style="top:273px"><span class="tick-box"></span>Immobilienbewertung</div>
    <div class="option" style="top:328px"><span class="tick-box"></span>Verwaltung von Immobilien</div>
    <div class="field" style="top:390px"></div>
    <p class="field-label" style="top:416px">Name</p>
    <div class="field" style="top:437px"></div>
    <p class="field-label" style="top:463px">Adresse</p>
    <div class="field" style="top:484px"></div>
    <p class="field-label" style="top:510px">Telefonnummer</p>
    <div class="divider"></div>
    <div class="stamp-box">Briefmarke</div>
    <p class="reply-service">Nordbrief Post<span>Antwort</span></p>
    <div class="client-logo">Logo von Ihnen</div>
    <p class="address">Ihre Daten wie<br>Name des Unternehmen<br>Straße<br>Postleitzahl &amp; Ort</p>
    <div class="back-band"></div>
  </section>
</body>
</html>
```